Webdesign für Hausverwaltung
Zielgruppe
Die BELMANOR Hausverwaltungs GmbH ist moderner Dienstleister, um die Werthaltigkeit von Immobilien zu sichern.
Egal ob Neu- oder Altbau, die Erfahrung im Gebäudemanagement richtet sich an institutionelle Anleger ebenso wie an Privatpersonen.
Aufgabenstellung
- Design als PSD erstellen, welches für Wordpress geeignet ist
- die Startseite layouten
- Im Mittelpunkt der Seite sollen die Wohnungsangebote, die aktuellen Meldungen und die Jobangebote stehen
- bitte stellen Sie ein Hinweisfenster dar, welches eingeblendet wird, wenn der Nutzer mehr als eine Minute auf der Seite verbleibt. (Slide out right- Popup) 'Sie haben Fragen? Wir helfen Ihnen gern' + Fenster zum Eintragen der Email

```html
<!DOCTYPE html>
<html lang="de">
<head>
<meta charset="utf-8">
<title>Belmanor Hausverwaltung – Startseite</title>
<link href="https://fonts.googleapis.com/css2?family=Poppins:wght@400;500;600;700&display=swap" rel="stylesheet">
<style>
:root{
  --navy:#0d1a8c;
  --band:#1126a3;
  --text:#4a4a4a;
  --muted:#7a7a7a;
  --card:#f3f3f3;
  --footer:#f0f0f0;
  --nav:#3d6b1f;
  --white:#ffffff;
}
*{margin:0;padding:0;box-sizing:border-box}
html,body{width:1200px;height:1200px;overflow:hidden;background:var(--white);font-family:'Poppins',sans-serif}
.stage{position:absolute;left:0;top:0;width:1920px;height:1920px;transform:scale(.625);transform-origin:0 0}
.page{position:absolute;left:688px;top:35px;width:556px;height:1880px;background:var(--white);box-shadow:0 0 14px rgba(0,0,0,.06)}
.abs{position:absolute}
.brand{left:14px;top:6px;font-size:17px;font-weight:600;color:var(--navy);letter-spacing:1px}
.nav{right:18px;top:23px;display:flex;gap:8px;font-size:5.5px;color:var(--nav)}
.nav span:first-child{color:var(--navy)}
.hero{left:0;top:35px;width:556px;height:268px;background:linear-gradient(100deg,#eef0f3 0%,#e6e4e2 40%,#c9c3bd 60%,#7d8fa8 85%,#f2f2f4 100%)}
.hero-title{left:18px;top:118px;font-size:18px;font-weight:700;color:var(--navy)}
.hero-text{left:18px;top:143px;width:200px;font-size:8.5px;line-height:10px;color:var(--text)}
.search{left:0;top:303px;width:556px;height:80px;background:var(--band);color:var(--white)}
.search h2{position:absolute;left:19px;top:12px;font-size:10.5px;font-weight:500}
.field{position:absolute;top:37px;font-size:6.5px;font-weight:500}
.field div{margin-top:2px;width:64px;height:10px;background:var(--white);color:var(--muted);font-size:4.5px;padding:2px 2px;font-weight:400}
.btn{position:absolute;left:415px;top:42px;width:86px;height:18px;border:1px solid var(--white);font-size:6.5px;text-align:center;line-height:16px}
.card{position:absolute;width:177px;height:190px;background:var(--card)}
.card .img{height:100px}
.card .t{position:absolute;left:5px;top:106px;font-size:8px;color:var(--text)}
.card .loc{position:absolute;left:14px;top:122px;font-size:6px;color:var(--text);display:flex;align-items:center;gap:6px}
.card .links{position:absolute;left:12px;top:138px;font-size:6px;color:var(--navy);display:flex;gap:8px}
.card .facts{position:absolute;left:20px;top:152px;width:140px;display:flex;justify-content:space-between;font-size:6px;color:var(--navy);text-align:center}
.card .facts div{width:36px}
.card svg.ic{display:block;margin:0 auto 4px}
.pager{top:802px;width:17px;height:13px;background:#ddd;font-size:6px;text-align:center;line-height:13px;color:var(--text)}
.center{left:0;width:556px;text-align:center;color:var(--navy)}
.news-h{top:864px;font-size:17px;font-weight:700}
.news-s{top:892px;font-size:9.5px;font-weight:500}
.news-img{top:926px;width:269px;height:155px}
.news-t{top:1088px;font-size:9px;font-weight:600;color:var(--navy)}
.news-p{top:1105px;width:255px;font-size:6.3px;line-height:7.5px;color:var(--text)}
.more{top:1143px;font-size:6.5px;font-weight:600;color:var(--navy)}
.team-h{top:1217px;font-size:17px;font-weight:700;line-height:20px}
.team-img{left:0;top:1286px;width:556px;height:220px;background:linear-gradient(90deg,#cfd4de 0%,#e9e4de 30%,#d8dde6 60%,#3a5ba8 85%,#c7ccd6 100%)}
.jobs-h{left:12px;top:1531px;font-size:16px;font-weight:700;color:var(--navy)}
.list{font-size:10px;font-weight:500;color:var(--navy);line-height:18px}
.apply{left:13px;top:1618px;font-size:13px;color:var(--navy);line-height:20px}
.apply b{font-weight:700}
.offer-h{left:367px;top:1530px;font-size:13px;font-weight:700;color:var(--navy)}
.footer{left:0;top:1734px;width:556px;height:146px;background:var(--footer);font-size:8px;color:var(--text);line-height:11px}
</style>
</head>
<body>
<div class="stage">
<div class="page">

  <div class="abs brand">BELMANOR</div>
  <nav class="abs nav"><span>Home</span><span>Unternehmen</span><span>Wohnungsangebote</span><span>News</span><span>Jobs</span><span>Referenzen</span><span>Downloads</span><span>Kontakt</span><span>Impressum</span><span>Datenschutz</span></nav>

  <div class="abs hero" role="img" aria-label="Foto: glückliches Paar mit Wohnungsschlüssel zwischen Umzugskartons"></div>
  <h1 class="abs hero-title">Verwaltung nach Maß</h1>
  <p class="abs hero-text">Durchsuchen Sie unser ständig wechselndes Angebot an Wohnungen nach Ihren individuellen Vorstellungen</p>

  <section class="abs search">
    <h2>Finden Sie Ihr Mietobjekt</h2>
    <div class="field" style="left:19px">Immobilienart<div>Mietwohnung</div></div>
    <div class="field" style="left:111px">Wohnort<div>alle</div></div>
    <div class="field" style="left:203px">Größe<div>bis 60 m2</div></div>
    <div class="field" style="left:291px">Preis<div>bis 1000€</div></div>
    <div class="btn">Suche starten</div>
  </section>

  <!-- Angebote Reihe 1 -->
  <div class="card" style="left:6px;top:402px">
    <div class="img" role="img" aria-label="Foto: weißes Mehrfamilienhaus" style="background:linear-gradient(180deg,#6f9bd6,#e8e8e8 55%,#8a6a4a)"></div>
    <div class="t">Ahornweg 15 WE 19</div>
    <div class="loc"><svg width="5" height="7" viewBox="0 0 10 14"><path d="M5 0a5 5 0 0 0-5 5c0 4 5 9 5 9s5-5 5-9a5 5 0 0 0-5-5z" fill="#444"/><circle cx="5" cy="5" r="2" fill="#f3f3f3"/></svg>Chemnitz, Schloßchemnitz</div>
    <div class="links"><span>Exposé bei Wohnportal</span><span>Exposé bei Mietfinder</span></div>
    <div class="facts"><div><svg class="ic" width="12" height="11"><rect x=".5" y=".5" width="11" height="10" fill="none" stroke="#999"/></svg>2</div><div><svg class="ic" width="12" height="11"><rect x=".5" y=".5" width="11" height="10" fill="none" stroke="#999"/></svg>48,5 m2</div><div><svg class="ic" width="12" height="11"><path d="M1 10V5l5-4 5 4v5z" fill="none" stroke="#999"/></svg>429,-€</div></div>
  </div>
  <div class="card" style="left:190px;top:402px">
    <div class="img" role="img" aria-label="Foto: ockerfarbenes Altbauhaus" style="background:linear-gradient(90deg,#8a8f6a,#d9a85a 40%,#b5816a)"></div>
    <div class="t">Birkenstraße 12 WE 3</div>
    <div class="loc"><svg width="5" height="7" viewBox="0 0 10 14"><path d="M5 0a5 5 0 0 0-5 5c0 4 5 9 5 9s5-5 5-9a5 5 0 0 0-5-5z" fill="#444"/><circle cx="5" cy="5" r="2" fill="#f3f3f3"/></svg>Chemnitz, Sonnberg</div>
    <div class="links"><span>Exposé bei Wohnportal</span><span>Exposé bei Mietfinder</span></div>
    <div class="facts"><div><svg class="ic" width="12" height="11"><rect x=".5" y=".5" width="11" height="10" fill="none" stroke="#999"/></svg>1</div><div><svg class="ic" width="12" height="11"><rect x=".5" y=".5" width="11" height="10" fill="none" stroke="#999"/></svg>33,32 m2</div><div><svg class="ic" width="12" height="11"><path d="M1 10V5l5-4 5 4v5z" fill="none" stroke="#999"/></svg>270,-€</div></div>
  </div>
  <div class="card" style="left:373px;top:402px">
    <div class="img" role="img" aria-label="Foto: rotes Backstein-Eckhaus" style="background:linear-gradient(180deg,#4f86d0,#c0584a 50%,#4f7a3a)"></div>
    <div class="t">Eichendorffstraße 8 WE 7</div>
    <div class="loc"><svg width="5" height="7" viewBox="0 0 10 14"><path d="M5 0a5 5 0 0 0-5 5c0 4 5 9 5 9s5-5 5-9a5 5 0 0 0-5-5z" fill="#444"/><circle cx="5" cy="5" r="2" fill="#f3f3f3"/></svg>Chemnitz, Zentrum</div>
    <div class="links"><span>Exposé bei Wohnportal</span><span>Exposé bei Mietfinder</span></div>
    <div class="facts"><div><svg class="ic" width="12" height="11"><rect x=".5" y=".5" width="11" height="10" fill="none" stroke="#999"/></svg>2</div><div><svg class="ic" width="12" height="11"><rect x=".5" y=".5" width="11" height="10" fill="none" stroke="#999"/></svg>52,38 m2</div><div><svg class="ic" width="12" height="11"><path d="M1 10V5l5-4 5 4v5z" fill="none" stroke="#999"/></svg>444,-€</div></div>
  </div>

  <!-- Angebote Reihe 2 -->
  <div class="card" style="left:6px;top:607px">
    <div class="img" role="img" aria-label="Foto: Gründerzeit-Eckhaus mit Herbstbaum" style="background:linear-gradient(180deg,#5d8fd2,#cdbfa6 55%,#8a6a3a)"></div>
    <div class="t">Mühlgasse 10 in 09113 Chemnitz WE 12</div>
    <div class="loc"><svg width="5" height="7" viewBox="0 0 10 14"><path d="M5 0a5 5 0 0 0-5 5c0 4 5 9 5 9s5-5 5-9a5 5 0 0 0-5-5z" fill="#444"/><circle cx="5" cy="5" r="2" fill="#f3f3f3"/></svg>Chemnitz, Schloßchemnitz</div>
    <div class="links"><span>Exposé bei Wohnportal</span><span>Exposé bei Mietfinder</span></div>
    <div class="facts"><div><svg class="ic" width="12" height="11"><rect x=".5" y=".5" width="11" height="10" fill="none" stroke="#999"/></svg>2</div><div><svg class="ic" width="12" height="11"><rect x=".5" y=".5" width="11" height="10" fill="none" stroke="#999"/></svg>50,6 m2</div><div><svg class="ic" width="12" height="11"><path d="M1 10V5l5-4 5 4v5z" fill="none" stroke="#999"/></svg>350,-€</div></div>
  </div>
  <div class="card" style="left:190px;top:607px">
    <div class="img" role="img" aria-label="Foto: gelbes Wohnhaus mit Balkonen" style="background:linear-gradient(180deg,#2f6fd0,#e8dca0 55%,#5b7a3a)"></div>
    <div class="t">Am Sonnenhang 7/7b WE 19</div>
    <div class="loc"><svg width="5" height="7" viewBox="0 0 10 14"><path d="M5 0a5 5 0 0 0-5 5c0 4 5 9 5 9s5-5 5-9a5 5 0 0 0-5-5z" fill="#444"/><circle cx="5" cy="5" r="2" fill="#f3f3f3"/></svg>Hartenstein</div>
    <div class="links"><span>Exposé bei Wohnportal</span><span>Exposé bei Mietfinder</span></div>
    <div class="facts"><div><svg class="ic" width="12" height="11"><rect x=".5" y=".5" width="11" height="10" fill="none" stroke="#999"/></svg>1</div><div><svg class="ic" width="12" height="11"><rect x=".5" y=".5" width="11" height="10" fill="none" stroke="#999"/></svg>32,21 m2</div><div><svg class="ic" width="12" height="11"><path d="M1 10V5l5-4 5 4v5z" fill="none" stroke="#999"/></svg>390,-€</div></div>
  </div>
  <div class="card" style="left:373px;top:607px">
    <div class="img" role="img" aria-label="Foto: helles Altbauhaus hinter Bäumen" style="background:linear-gradient(90deg,#6f9a4a,#d8d6c8 50%,#9fb4c8)"></div>
    <div class="t">Lerchenweg 39 WE 5</div>
    <div class="loc"><svg width="5" height="7" viewBox="0 0 10 14"><path d="M5 0a5 5 0 0 0-5 5c0 4 5 9 5 9s5-5 5-9a5 5 0 0 0-5-5z" fill="#444"/><circle cx="5" cy="5" r="2" fill="#f3f3f3"/></svg>Chemnitz, Kaßberg</div>
    <div class="links"><span>Exposé bei Wohnportal</span><span>Exposé bei Mietfinder</span></div>
    <div class="facts"><div><svg class="ic" width="12" height="11"><rect x=".5" y=".5" width="11" height="10" fill="none" stroke="#999"/></svg>2</div><div><svg class="ic" width="12" height="11"><rect x=".5" y=".5" width="11" height="10" fill="none" stroke="#999"/></svg>49,48 m2</div><div><svg class="ic" width="12" height="11"><path d="M1 10V5l5-4 5 4v5z" fill="none" stroke="#999"/></svg>447,-€</div></div>
  </div>
  <div class="abs pager" style="left:512px">1</div>
  <div class="abs pager" style="left:532px;background:#e6e6e6">2</div>

  <!-- News -->
  <h2 class="abs center news-h">News - Aktuelle Meldungen</h2>
  <p class="abs center news-s">Risus commodo viverra maecenas accumsan lacus vel facilisis.</p>
  <div class="abs news-img" style="left:6px;background:linear-gradient(90deg,#e4e6e8,#b9bcbf 50%,#c9b7a0)" role="img" aria-label="Foto: modernes Großraumbüro mit Konferenztisch"></div>
  <div class="abs news-img" style="left:280px;background:linear-gradient(90deg,#d9d6d0,#c89a7a 45%,#4a6a9a 70%,#2e2a28)" role="img" aria-label="Foto: Beratungsgespräch mit Handschlag"></div>
  <h3 class="abs news-t" style="left:6px">Wir vermieten auch Büroflächen</h3>
  <h3 class="abs news-t" style="left:280px">Wir beraten Sie umfangreich bei der Wohnungssuche</h3>
  <p class="abs news-p" style="left:6px">Lorem ipsum dolor sit amet, consectetur adipiscing elit, sed do eiusmod tempor incididunt ut labore et dolore magna aliqua. Quis ipsum suspendisse ultrices gravida. Risus commodo viverra maecenas accumsan lacus vel facilisis.</p>
  <p class="abs news-p" style="left:280px">Lorem ipsum dolor sit amet, consectetur adipiscing elit, sed do eiusmod tempor incididunt ut labore et dolore magna aliqua. Quis ipsum suspendisse ultrices gravida. Risus commodo viverra maecenas accumsan lacus vel facilisis.</p>
  <span class="abs more" style="left:6px">Weiterlesen</span>
  <span class="abs more" style="left:280px">Weiterlesen</span>

  <!-- Jobs -->
  <h2 class="abs center team-h">Sie möchten ein Teil unseres Teams werden?<br>Dann bewerben Sie sich jetzt</h2>
  <div class="abs team-img" role="img" aria-label="Foto: Bewerbungsgespräch, Bewerberin mit Mappe im Büro"></div>
  <h2 class="abs jobs-h">Aktuelle Jobangebote</h2>
  <div class="abs list" style="left:13px;top:1560px">- Kundenberater/innen<br>- Reinigungskraft</div>
  <p class="abs apply">Richten Sie Ihre Bewerbung an<br><b>info@belmanor-hv.de</b></p>
  <h3 class="abs offer-h">Was wir bieten</h3>
  <div class="abs list" style="left:367px;top:1558px;line-height:17px">- flexible Arbeitszeiten<br>- sicherer Arbeitsplatz<br>- Weiterbildungen<br>- Benefits<br>- uvm.</div>

  <!-- Footer -->
  <footer class="abs footer">
    <div class="abs" style="left:18px;top:20px"><b style="font-weight:600">Belmanor Hausverwaltung</b><br><span style="line-height:20px">Lindenhofstraße 12</span><br><span style="position:relative;top:-9px">09114 Chemnitz</span></div>
    <div class="abs" style="left:18px;top:68px">Tel.: 0 371 555-0142<br><span style="line-height:20px">info@belmanor-hv.de</span></div>
    <svg class="abs" style="left:269px;top:57px" width="14" height="14"><circle cx="7" cy="7" r="6" fill="none" stroke="#666" stroke-width="1.2"/></svg>
    <div class="abs" style="left:248px;top:78px;width:60px;height:12px;background:#cfd8dc;border-radius:2px" role="img" aria-label="Partnerzeichen"></div>
    <div class="abs" style="left:441px;top:38px">Downloads<br>FAQS</div>
    <div class="abs" style="left:441px;top:72px">Impressum<br>Datenschutz</div>
    <div class="abs" style="left:441px;top:118px;font-size:4.5px">copyright Belmanor HV</div>
  </footer>

</div>
</div>
</body>
</html>
```